KALVERIA Consultancy Business Card

We need a business card design for a new Image & Etiquette Consultancy Company.

The design should reflect the corporate colour found in the logo attached.

Info to include:

Name: Melba Tran
Title: Image Consultant
Company: KAL VERIA CONSULTANCY
Address: 27 Kelso Street, #14-09 Harbourline Tower, Singapore 058217
Contact: 9317 6284
Email: melba@kalveria.com.sg
Website: www.kalveria.com.sg

```html
<!DOCTYPE html>
<html lang="en">
<head>
<meta charset="utf-8">
<title>KALVERIA Consultancy Business Card</title>
<link href="https://fonts.googleapis.com/css2?family=Michroma&family=Exo+2:wght@400;500;600&display=swap" rel="stylesheet">
<style>
  :root {
    --stage: #e9e9ea;
    --plum: #3f2a4f;
    --gold: #c9a03a;
    --gold-light: #ecca6a;
    --ink: #2b2730;
    --grey: #8b8790;
    --paper: #ffffff;
  }
  * { margin: 0; padding: 0; box-sizing: border-box; }
  html, body { width: 1200px; height: 854px; overflow: hidden; }
  body {
    background: var(--stage);
    position: relative;
    font-family: "Exo 2", sans-serif;
  }
  .card { position: absolute; overflow: hidden; box-shadow: 0 10px 26px rgba(0,0,0,.18); }
  .card-back { left: 90px; top: 257px; width: 600px; height: 340px; background: var(--plum); }
  .card-front { left: 780px; top: 127px; width: 340px; height: 600px; background: var(--paper); }
  .card svg.shapes { position: absolute; inset: 0; width: 100%; height: 100%; }

  .back-brand { position: absolute; left: 0; right: 0; top: 128px; text-align: center; }
  .brand-name {
    font-family: "Michroma", sans-serif;
    color: var(--gold);
    font-size: 46px;
    letter-spacing: 4px;
    line-height: 1;
  }
  .brand-sub {
    font-family: "Michroma", sans-serif;
    color: #a9a3b0;
    font-size: 13px;
    letter-spacing: 5px;
    margin-top: 10px;
  }

  .front-brand { position: absolute; left: 0; right: 0; top: 58px; text-align: center; }
  .front-brand .brand-name { color: var(--plum); font-size: 30px; letter-spacing: 3px; }
  .tagline {
    color: var(--gold);
    font-size: 9px;
    letter-spacing: 2px;
    text-transform: uppercase;
    margin-top: 8px;
  }

  .holder { position: absolute; left: 0; right: 0; top: 158px; text-align: center; }
  .holder-name {
    font-family: "Michroma", sans-serif;
    color: var(--ink);
    font-size: 22px;
    letter-spacing: 1px;
  }
  .holder-title {
    color: var(--gold);
    font-size: 11px;
    letter-spacing: 2px;
    text-transform: uppercase;
    margin-top: 6px;
  }

  .contacts { position: absolute; left: 64px; top: 258px; list-style: none; }
  .contacts li {
    display: flex; align-items: center; gap: 10px;
    font-size: 13px; color: var(--ink); letter-spacing: .5px;
    margin-bottom: 12px;
  }
  .contact-icon { width: 18px; height: 18px; flex: none; }

  .address {
    position: absolute; left: 40px; right: 30px; top: 470px;
    color: var(--paper);
    font-size: 15px; font-weight: 600; line-height: 1.45; letter-spacing: .5px;
  }
</style>
</head>
<body>

<div class="card card-back">
  <svg class="shapes" viewBox="0 0 600 340" aria-hidden="true">
    <defs>
      <linearGradient id="goldBack" x1="0" x2="1" y1="0" y2="0">
        <stop offset="0" stop-color="#b8892a"/>
        <stop offset=".5" stop-color="#f0d27a"/>
        <stop offset="1" stop-color="#b8892a"/>
      </linearGradient>
    </defs>
    <path d="M96 0 H600 V16 H104 A8 8 0 0 1 96 8 Z" fill="url(#goldBack)"/>
    <path d="M0 230 H8 A8 8 0 0 1 16 238 V340 H0 Z" fill="url(#goldBack)"/>
  </svg>
  <div class="back-brand">
    <div class="brand-name">KALVERIA</div>
    <div class="brand-sub">CONSULTANCY</div>
  </div>
</div>

<div class="card card-front">
  <svg class="shapes" viewBox="0 0 340 600" aria-hidden="true">
    <defs>
      <linearGradient id="goldFront" x1="0" x2="1" y1="0" y2="0">
        <stop offset="0" stop-color="#b8892a"/>
        <stop offset=".5" stop-color="#f0d27a"/>
        <stop offset="1" stop-color="#b8892a"/>
      </linearGradient>
    </defs>
    <path d="M0 410 C110 400 250 425 340 500 V600 H0 Z" fill="var(--plum)"/>
    <rect x="22" y="584" width="318" height="16" rx="8" fill="url(#goldFront)"/>
  </svg>

  <div class="front-brand">
    <div class="brand-name">KALVERIA</div>
    <div class="tagline">Image and Etiquette Consultancy</div>
  </div>

  <div class="holder">
    <div class="holder-name">MELBA TRAN</div>
    <div class="holder-title">Image Consultant</div>
  </div>

  <ul class="contacts">
    <li>
      <svg class="contact-icon" viewBox="0 0 18 18" aria-hidden="true"><circle cx="9" cy="9" r="9" fill="var(--gold)"/><path d="M6 5 l2 0 l1 2.5 -1.2 1 a5 5 0 0 0 2.7 2.7 l1-1.2 2.5 1 0 2 a1 1 0 0 1-1 1 A8 8 0 0 1 5 6 a1 1 0 0 1 1-1z" fill="#fff"/></svg>
      9317 6284
    </li>
    <li>
      <svg class="contact-icon" viewBox="0 0 18 18" aria-hidden="true"><circle cx="9" cy="9" r="9" fill="var(--gold)"/><rect x="4.5" y="6" width="9" height="6.5" rx="1" fill="#fff"/><path d="M4.8 6.3 L9 9.5 L13.2 6.3" stroke="var(--gold)" stroke-width="1" fill="none"/></svg>
      melba@kalveria.com.sg
    </li>
    <li>
      <svg class="contact-icon" viewBox="0 0 18 18" aria-hidden="true"><circle cx="9" cy="9" r="9" fill="var(--gold)"/><circle cx="9" cy="9" r="4.5" fill="none" stroke="#fff" stroke-width="1.2"/><path d="M4.5 9 H13.5 M9 4.5 C7 7 7 11 9 13.5 C11 11 11 7 9 4.5" fill="none" stroke="#fff" stroke-width="1"/></svg>
      www.kalveria.com.sg
    </li>
  </ul>

  <p class="address">27 Kelso Street, #14-09<br>Harbourline Tower,<br>Singapore 058217</p>
</div>

</body>
</html>
```